Letterhead design - Harwick Group

We have just had our Logo created and our now wantng a letterhead design to incorporate this. Please use the same colours as in the logo, which is attached.
Please use the company details below
P O Box 86, Bleneheim 7315
Ph: 03 642 1937
dave@harwickgroup.co.nz
We would like a professional look
We need an overall letterhead design for our varied group of buisinesses which are based in NZ and overseas. We grow and develop buisinesses. Our companies began in NZ but we now have branches overseas as well. People are our greatest asset and we employ some incredible staff. Our buisinesses are scientific, innovative and growing in size and expertise with a financial base.

Target Market(s)

Professionals

Industry/Entity Type

Investment

Requirements
Must have
• Easy to read.
• Please use the same colours as in the logo
• Please use the company details below
• P O Box 86, Bleneheim 7315
• Ph: 03 642 1937
• dave@harwickgroup.co.nz

```html
<!DOCTYPE html>
<html lang="en">
<head>
<meta charset="utf-8">
<title>Harwick Group – Letterhead</title>
<link rel="stylesheet" href="https://fonts.googleapis.com/css2?family=Lato:wght@400;700&display=swap">
<style>
  :root {
    --canvas: #ffffff;
    --page: #ffffff;
    --page-edge: #d9d9d9;
    --band: #666666;
    --brand-green: #27b673;
    --brand-grey: #666666;
    --strip-text: #ffffff;
    --rail: #ffffff;
  }
  html, body {
    margin: 0;
    padding: 0;
    width: 1200px;
    height: 1000px;
    overflow: hidden;
    background: var(--canvas);
    font-family: "Lato", sans-serif;
  }
  .letterhead {
    position: absolute;
    left: 211px;
    top: 0;
    width: 778px;
    height: 999px;
    background: var(--page);
    border: 1px solid var(--page-edge);
    box-sizing: border-box;
    overflow: hidden;
  }
  .side-band {
    position: absolute;
    left: 0;
    top: 0;
    width: 92px;
    height: 100%;
    background: var(--band);
  }
  .brand {
    position: absolute;
    left: 447px;
    top: 35px;
    display: flex;
    align-items: center;
    gap: 10px;
  }
  .brand-mark {
    width: 55px;
    height: 55px;
    background: var(--brand-grey);
  }
  .brand-name {
    font-weight: 700;
    font-size: 26px;
    letter-spacing: 0.5px;
    color: var(--brand-green);
    text-transform: uppercase;
    line-height: 1;
    white-space: nowrap;
  }
  .contact-rail {
    position: absolute;
    left: 44px;
    top: 814px;
    width: 3px;
    height: 174px;
    background: var(--rail);
  }
  .contact-list {
    position: absolute;
    left: 46px;
    top: 836px;
    margin: 0;
    padding: 0;
    list-style: none;
  }
  .contact-item {
    position: relative;
    height: 32px;
    margin-bottom: 17px;
    color: var(--strip-text);
    font-size: 15px;
    line-height: 32px;
  }
  .contact-item svg.strip {
    position: absolute;
    left: 0;
    top: 0;
  }
  .contact-icon {
    position: absolute;
    left: 11px;
    top: 5px;
    width: 22px;
    height: 22px;
  }
  .contact-text {
    position: absolute;
    left: 100px;
    top: 0;
    white-space: nowrap;
  }
</style>
</head>
<body>
  <main class="letterhead">
    <div class="side-band"></div>

    <header class="brand">
      <div class="brand-mark"></div>
      <div class="brand-name">Harwick Group</div>
    </header>

    <div class="contact-rail"></div>
    <ul class="contact-list">
      <li class="contact-item">
        <svg class="strip" width="290" height="32" viewBox="0 0 290 32"><polygon points="0,0 275,0 290,32 0,32" fill="var(--brand-green)"/></svg>
        <svg class="contact-icon" viewBox="0 0 24 24" aria-hidden="true"><path fill="#fff" d="M6.6 10.8c1.4 2.8 3.8 5.1 6.6 6.6l2.2-2.2c.3-.3.7-.4 1-.2 1.1.4 2.3.6 3.6.6.6 0 1 .4 1 1V20c0 .6-.4 1-1 1C10.6 21 3 13.4 3 4c0-.6.4-1 1-1h3.5c.6 0 1 .4 1 1 0 1.2.2 2.4.6 3.6.1.3 0 .7-.2 1L6.6 10.8z"/></svg>
        <span class="contact-text">03 642 1937</span>
      </li>
      <li class="contact-item">
        <svg class="strip" width="313" height="32" viewBox="0 0 313 32"><polygon points="0,0 298,0 313,32 0,32" fill="var(--brand-green)"/></svg>
        <svg class="contact-icon" viewBox="0 0 24 24" aria-hidden="true"><rect x="3" y="6" width="18" height="12" fill="#fff"/><polyline points="3,6 12,13 21,6" fill="none" stroke="var(--brand-green)" stroke-width="1.4"/></svg>
        <span class="contact-text">dave@harwickgroup.co.nz</span>
      </li>
      <li class="contact-item">
        <svg class="strip" width="336" height="32" viewBox="0 0 336 32"><polygon points="0,0 321,0 336,32 0,32" fill="var(--brand-green)"/></svg>
        <svg class="contact-icon" viewBox="0 0 24 24" aria-hidden="true"><path fill="#fff" d="M12 2C8.1 2 5 5.1 5 9c0 5.2 7 13 7 13s7-7.8 7-13c0-3.9-3.1-7-7-7zm0 9.5c-1.4 0-2.5-1.1-2.5-2.5S10.6 6.5 12 6.5s2.5 1.1 2.5 2.5-1.1 2.5-2.5 2.5z"/></svg>
        <span class="contact-text">P O Box 86, Kelmont 7315</span>
      </li>
    </ul>
  </main>
</body>
</html>
```